Civic Holdwell Business Card

We are looking to design new business cards for our company. We have two office locations and would like to have both full addresses on the card. Each address needs two lines for the building name and street address and a line or two for the city, state and zip code. There should be a place for 2-3 phone numbers. The addresses and phone numbers are at the bottom of this description. We also need a place to put our company website and one email address. Our logo is attached.
We would like the card to be two sided. The back of the card should have a blue background with some part of our logo design on it. We would like the full logo on the front of the card as well. The front of the card should have a white background with the blue logo. We are open to listing our addresses on the front or the back of the card. The person who designed our logo gave us an excellent business card idea that we really liked. I have attached a picture of his business card idea so that we can build off of it.
Addresses:
The Tanner Hall
2184 17th Street NW
Washington, DC 20007
Marlow Crest Tower
410 Dorsen Avenue #2215
Miami, FL 33131
Phone Numbers: (202) 555-0148
(202) 555-0193
Website: www.civicholdwell.example

```html
<!DOCTYPE html>
<html lang="en">
<head>
<meta charset="utf-8">
<title>Civic Holdwell Business Card</title>
<link rel="stylesheet" href="https://fonts.googleapis.com/css2?family=Open+Sans:wght@400;600;700&display=swap">
<style>
  :root {
    --brand-blue: #202a7c;
    --brand-blue-deep: #1b2470;
    --charcoal: #232326;
    --paper: #f4f4f4;
    --ink: #2a2a2e;
    --stage: #8c8c8c;
    --white: #ffffff;
  }
  * { box-sizing: border-box; margin: 0; padding: 0; }
  html, body {
    width: 1200px; height: 900px; overflow: hidden;
    background: var(--stage);
    font-family: "Open Sans", Arial, sans-serif;
  }
  .canvas {
    width: 1200px; height: 900px;
    display: flex; align-items: center; justify-content: center; gap: 40px;
  }
  .card {
    position: relative;
    width: 540px; height: 308px;
    overflow: hidden;
    box-shadow: 0 6px 18px rgba(0,0,0,0.3);
  }

  /* Front */
  .card-front { background: linear-gradient(135deg, #fafafa, #e9e9e9); color: var(--ink); }
  .edge-blue { position: absolute; left: 0; top: 0; bottom: 0; width: 12px; background: var(--brand-blue); }
  .edge-dark {
    position: absolute; left: 12px; top: 0; bottom: 0; width: 22px; background: var(--charcoal);
    display: flex; flex-direction: column; align-items: center; justify-content: flex-end;
    gap: 9px; padding-bottom: 14px;
  }
  .edge-dark svg { width: 11px; height: 11px; fill: var(--white); }
  .front-logo {
    position: absolute; right: 34px; top: 38px;
    display: flex; align-items: center; gap: 10px;
  }
  .logo-square { width: 40px; height: 40px; border-radius: 5px; background: var(--brand-blue); }
  .logo-name {
    font-weight: 600; font-size: 30px; letter-spacing: 1px;
    text-transform: uppercase; color: var(--brand-blue); line-height: 1;
  }
  .divider-blue {
    position: absolute; left: 34px; right: 0; top: 112px; height: 1.5px; background: var(--brand-blue);
  }
  .addresses {
    position: absolute; top: 130px; right: 26px; display: flex; gap: 36px;
    font-size: 11.5px; line-height: 1.45;
  }
  .person {
    position: absolute; left: 52px; bottom: 30px; font-size: 12px; line-height: 1.5;
  }
  .person-name {
    font-weight: 700; font-size: 13px; padding-bottom: 4px; margin-bottom: 6px;
    border-bottom: 1.5px solid var(--brand-blue); width: 160px;
  }

  /* Back */
  .card-back { background: var(--brand-blue); color: var(--white); }
  .back-logo {
    position: absolute; left: 0; right: 0; top: 92px;
    display: flex; align-items: center; justify-content: center; gap: 12px;
  }
  .back-logo .logo-square { background: var(--white); width: 46px; height: 46px; }
  .back-logo .logo-name { color: var(--white); font-size: 36px; }
  .divider-white { position: absolute; left: 0; right: 0; top: 212px; height: 1px; background: var(--white); }
  .website {
    position: absolute; left: 0; right: 0; top: 238px; text-align: center;
    font-size: 14px; letter-spacing: 2.5px;
  }
  .website strong { font-weight: 700; }
</style>
</head>
<body>
<main class="canvas">
  <section class="card card-front" aria-label="Front of business card">
    <div class="edge-blue"></div>
    <div class="edge-dark">
      <svg viewBox="0 0 12 12" aria-hidden="true"><circle cx="6" cy="6" r="4"/></svg>
      <svg viewBox="0 0 12 12" aria-hidden="true"><path d="M3 1l2 3-1.3 1.2a7 7 0 0 0 3.1 3.1L8 7l3 2-1 2C5 11 1 7 1 2z"/></svg>
      <svg viewBox="0 0 12 12" aria-hidden="true"><rect x="3" y="1" width="6" height="3"/><rect x="1" y="5" width="10" height="4"/><rect x="3" y="8" width="6" height="3"/></svg>
      <svg viewBox="0 0 12 12" aria-hidden="true"><path d="M1 3h10v7H1z M1 3l5 4 5-4" stroke="#232326" stroke-width="0.8"/></svg>
    </div>
    <div class="front-logo">
      <span class="logo-square"></span>
      <span class="logo-name">Civic Holdwell</span>
    </div>
    <div class="divider-blue"></div>
    <div class="addresses">
      <address class="office" style="font-style:normal">Marlow Crest Tower<br>410 Dorsen Avenue #2215<br>Miami, FL 33131</address>
      <address class="office" style="font-style:normal">The Tanner Hall<br>2184 17th Street NW<br>Washington, DC 20007</address>
    </div>
    <div class="person">
      <div class="person-name">Daniel Marsh</div>
      <div>(202) 555-0148</div>
      <div>(202) 555-0193</div>
      <div>info@civicholdwell.example</div>
    </div>
  </section>

  <section class="card card-back" aria-label="Back of business card">
    <div class="back-logo">
      <span class="logo-square"></span>
      <span class="logo-name">Civic Holdwell</span>
    </div>
    <div class="divider-white"></div>
    <p class="website">www.<strong>civicholdwell</strong>.example</p>
  </section>
</main>
</body>
</html>
```